Bramblegate Card Company Business Cards

We are a trading card store with Zorvanix, sports and other TCG cards, we need a business card design that encompasses a clean cut, modern style with a retro flare. website is bramblegatecardco.example for reference. Can utilize a comic book era feel or a more modern outdoor feel to utilize the "Pacific Northwest" elements of tress, mountains, etc.

Industry/Entity Type

Trading cards and collectibles

Contact Information for Business Card

business name, email address, phone number, name, owner job title

Font styles to use
Sans Serif

```html
<!DOCTYPE html>
<html lang="en">
<head>
<meta charset="utf-8">
<title>Bramblegate Card Company – Business Cards</title>
<link rel="stylesheet" href="https://fonts.googleapis.com/css2?family=Open+Sans:wght@400;600;700&display=swap">
<style>
  :root {
    --bg: #2b2b2b;
    --card-white: #f3f3f3;
    --card-grey: #666666;
    --band-grey: #5f5f5f;
    --ink-grey: #5a5a5a;
    --accent-blue: #19a9d3;
    --faint-grey: #e2e2e2;
    --white: #ffffff;
  }
  * { box-sizing: border-box; margin: 0; padding: 0; }
  html, body { width: 1200px; height: 873px; overflow: hidden; }
  body {
    background: var(--bg);
    font-family: "Open Sans", sans-serif;
    position: relative;
  }
  .card {
    position: absolute;
    top: 283px;
    width: 540px;
    height: 306px;
    box-shadow: 0 10px 28px rgba(0,0,0,0.45);
    overflow: hidden;
  }
  .card--front { left: 40px; background: var(--card-white); }
  .card--back { left: 620px; background: var(--card-grey); }

  .front-waves { position: absolute; inset: 0; }
  .front-mountain-fade {
    position: absolute;
    left: 300px; top: 195px;
    width: 200px; height: 65px;
    background: linear-gradient(180deg, rgba(226,226,226,0) 0%, var(--faint-grey) 100%);
  }

  .brand-name {
    position: absolute;
    text-align: center;
    font-weight: 700;
    letter-spacing: 1px;
    line-height: 1.25;
  }
  .card--front .brand-name {
    left: 70px; top: 112px; width: 170px;
    color: var(--ink-grey);
    font-size: 16px;
  }
  .brand-name .brand-mark {
    display: block;
    width: 34px; height: 34px;
    margin: 0 auto 8px;
    border-radius: 50%;
    background: currentColor;
  }
  .brand-name .brand-sub { font-size: 11px; letter-spacing: 2px; }

  .divider {
    position: absolute;
    left: 255px; top: 112px;
    width: 1.5px; height: 84px;
    background: var(--accent-blue);
  }
  .contact { position: absolute; left: 290px; top: 112px; color: var(--ink-grey); }
  .contact-name {
    color: var(--accent-blue);
    font-weight: 700;
    font-size: 17px;
    letter-spacing: 0.3px;
  }
  .contact-title { font-size: 12px; margin-top: -2px; }
  .contact-list { list-style: none; margin-top: 18px; font-size: 12px; line-height: 1.45; }
  .contact-list li { display: flex; align-items: center; gap: 6px; }
  .contact-list svg { width: 10px; height: 10px; fill: var(--accent-blue); }

  .front-url {
    position: absolute;
    left: 92px; bottom: 10px;
    color: var(--white);
    font-size: 12px;
  }

  .card--back .brand-name {
    left: 170px; top: 78px; width: 200px;
    color: var(--white);
    font-size: 20px;
  }
  .back-url {
    position: absolute;
    left: 0; right: 0; bottom: 38px;
    text-align: center;
    color: var(--white);
    font-size: 12px;
  }
</style>
</head>
<body>

  <section class="card card--front" aria-label="Business card front">
    <div class="front-mountain-fade" role="img" aria-label="Faint mountain range decoration"></div>
    <svg class="front-waves" viewBox="0 0 540 306" aria-hidden="true">
      <path d="M0,282 C120,255 250,255 360,262 C440,268 500,258 540,248 L540,306 L0,306 Z" fill="var(--band-grey)"/>
      <path d="M0,270 C80,246 160,242 230,250 C160,250 80,262 0,282 Z" fill="var(--accent-blue)"/>
      <path d="M400,262 C460,262 510,252 540,236 L540,248 C500,258 450,264 400,262 Z" fill="var(--accent-blue)"/>
    </svg>

    <div class="brand-name">
      <span class="brand-mark"></span>
      BRAMBLEGATE<br><span class="brand-sub">CARD COMPANY</span>
    </div>

    <div class="divider"></div>

    <div class="contact">
      <p class="contact-name">MARCUS ELLERY</p>
      <p class="contact-title">Managing Director</p>
      <ul class="contact-list">
        <li>
          <svg viewBox="0 0 10 10"><path d="M2,0 L4,2.5 L3,3.5 C3.6,5 5,6.4 6.5,7 L7.5,6 L10,8 L8.5,10 C4,9.5 0.5,6 0,1.5 Z"/></svg>
          555.010.200
        </li>
        <li>
          <svg viewBox="0 0 10 10"><path d="M0,2 H10 V8 H0 Z M0,2 L5,5.5 L10,2" fill="var(--accent-blue)"/><path d="M0.8,2.4 L5,5.2 L9.2,2.4" stroke="var(--white)" stroke-width="0.8" fill="none"/></svg>
          info@bramblegatecardco.example
        </li>
      </ul>
    </div>

    <p class="front-url">www.bramblegatecardco.example</p>
  </section>

  <section class="card card--back" aria-label="Business card back">
    <div class="brand-name">
      <span class="brand-mark"></span>
      BRAMBLEGATE<br><span class="brand-sub">CARD COMPANY</span>
    </div>
    <p class="back-url">www.bramblegatecardco.example</p>
  </section>

</body>
</html>
```